Postcard Design

Landscaping Company
Lawn Cuts
Mulch
Spring Clean Ups
Planting

Company Name - RTM GROUNDWORK SERVICES
ADDRESS - 47 Dunmore Ln.
W. Pellston, NJ 08591
Phone #- 609-555-0148

Target Market(s)

Direct mailer looking to draw in new clients

Industry/Entity Type

It Company

Requirements
Must have
• Eye catching

```html
<!DOCTYPE html>
<html lang="en">
<head>
<meta charset="utf-8">
<title>RTM Groundwork Services Postcard</title>
<link rel="stylesheet" href="https://fonts.googleapis.com/css2?family=Arimo:wght@400;700&family=Lato:wght@400;700&family=Teko:wght@500&family=Tinos&display=swap">
<style>
  :root {
    --bg: #ebebeb;
    --green: #4f9a3a;
    --green-dark: #3b7a2a;
    --green-light: #62ad4a;
    --ink: #4a4d52;
    --arc: #4a4a4a;
    --white: #ffffff;
    --stamp: #c9cdcf;
    --accent: #4b7bb8;
  }
  * { box-sizing: border-box; margin: 0; padding: 0; }
  html, body { width: 1200px; height: 1200px; overflow: hidden; }
  body { background: var(--bg); position: relative; font-family: "Lato", sans-serif; }

  .card { position: absolute; width: 680px; height: 510px; overflow: hidden; background: var(--white); }
  .card--front { left: 50px; top: 50px; }
  .card--back { left: 470px; top: 610px; }
  .card-shape { position: absolute; inset: 0; width: 680px; height: 510px; }

  .side-label { position: absolute; font-family: "Arimo", sans-serif; font-size: 30px; color: #222; }
  .side-label--front { left: 140px; top: 590px; }
  .side-label--back { left: 1080px; top: 1140px; }

  .photo { position: absolute; border: 3px solid var(--white); border-radius: 14px; box-shadow: 0 0 0 2px var(--green-dark); }
  .photo--hero { border: 0; border-radius: 0; box-shadow: none; left: 0; top: 0; width: 680px; height: 510px;
    background: linear-gradient(180deg, #cfe2f2 0%, #b9d2e6 25%, #8e9a86 42%, #a9a392 60%, #8a8272 80%, #5e6b4a 100%); }
  .photo--apartments { left: 431px; top: 49px; width: 158px; height: 101px;
    background: linear-gradient(180deg, #a9cbe8 0%, #c99a6a 45%, #b07a4e 75%, #6f8f55 100%); }
  .photo--house { left: 361px; top: 197px; width: 161px; height: 97px;
    background: linear-gradient(180deg, #8fb6dc 0%, #d7cdb8 45%, #b8ab94 70%, #5f8a3f 100%); }
  .photo--garden { left: 222px; top: 287px; width: 160px; height: 100px;
    background: linear-gradient(180deg, #a8c8a0 0%, #7d7466 40%, #9a8a78 62%, #5d9142 85%, #c45a8a 100%); }

  .brand { position: absolute; display: flex; align-items: center; gap: 10px; color: var(--ink);
    font-family: "Arimo", sans-serif; line-height: 1; }
  .brand-mark { width: 34px; height: 34px; border: 3px solid var(--accent); flex: none; }
  .brand-name { display: flex; flex-direction: column; }
  .brand-name-main { font-weight: 700; font-size: 46px; letter-spacing: -1px; }
  .brand-name-sub { font-weight: 400; font-size: 19px; margin-top: 2px; }
  .card--front .brand { left: 28px; top: 36px; }
  .card--back .brand { left: 360px; top: 28px; gap: 8px; }
  .card--back .brand-mark { width: 28px; height: 28px; }
  .card--back .brand-name-main { font-size: 38px; }
  .card--back .brand-name-sub { font-size: 15px; }

  .contact-pill { position: absolute; left: 0; top: 346px; width: 218px; height: 62px;
    background: rgba(79, 154, 58, 0.92); border-radius: 0 14px 14px 0; padding: 6px 0 0 20px;
    font-family: "Tinos", serif; font-size: 12px; color: var(--white); }
  .contact-row { display: flex; align-items: center; gap: 7px; height: 17px; white-space: nowrap; }
  .contact-row svg { width: 10px; height: 10px; flex: none; }

  .hours { position: absolute; left: 57px; top: 474px; font-family: "Teko", sans-serif; font-weight: 500;
    font-size: 22px; color: var(--white); letter-spacing: 0.5px; line-height: 1; }

  .section-title { position: absolute; font-family: "Teko", sans-serif; font-weight: 500; font-size: 22px;
    line-height: 1; color: var(--white); padding: 2px 14px 0 10px; border-left: 2px solid var(--white);
    border-bottom: 2px solid var(--white); letter-spacing: 0.5px; }
  .body-copy { position: absolute; font-size: 11.5px; line-height: 14px; color: var(--white); }

  .mission-title { left: 470px; top: 316px; }
  .mission-copy { left: 425px; top: 348px; width: 232px; }

  .services-title { left: 46px; top: 28px; }
  .services-copy { left: 27px; top: 60px; width: 270px; }
  .why-title { left: 46px; top: 204px; }
  .why-copy { left: 27px; top: 238px; width: 272px; }
  .checklist { position: absolute; left: 27px; top: 276px; list-style: none; font-size: 12.5px;
    line-height: 16px; color: var(--white); }
  .checklist li { position: relative; padding-left: 16px; }
  .checklist li::before { content: ""; position: absolute; left: 2px; top: 2px; width: 5px; height: 9px;
    border-right: 2.5px solid var(--white); border-bottom: 2.5px solid var(--white); transform: rotate(40deg); }
  .clients-title { left: 46px; top: 388px; }

  .client-list { position: absolute; left: 44px; top: 424px; display: flex; gap: 18px; list-style: none; }
  .client { width: 74px; text-align: center; }
  .client-box { height: 38px; background: var(--white); border-radius: 4px; display: flex; align-items: center;
    justify-content: center; font-size: 9.5px; font-weight: 700; color: var(--green-dark); line-height: 1.1; padding: 0 3px; }
  .client-caption { margin-top: 6px; font-size: 8px; line-height: 10px; color: var(--white); }

  .stamp-box { position: absolute; left: 584px; top: 30px; width: 61px; height: 75px; background: var(--stamp); border-radius: 4px; }
  .address-lines { position: absolute; left: 400px; top: 208px; width: 245px; }
  .address-lines span { display: block; height: 2px; background: #222; margin-bottom: 30px; }
  .return-address { position: absolute; right: 36px; top: 370px; text-align: right; font-family: "Arimo", sans-serif;
    font-size: 11.5px; line-height: 14.5px; color: #111; font-style: normal; }
  .return-address strong { display: block; font-size: 12px; margin-bottom: 9px; }
</style>
</head>
<body>

<section class="card card--front" aria-label="Postcard front">
  <div class="photo photo--hero" role="img" aria-label="Photo of a multi-storey residential apartment building under a blue sky"></div>
  <svg class="card-shape" viewBox="0 0 680 510" aria-hidden="true">
    <defs>
      <linearGradient id="frontGreen" x1="0" y1="0" x2="1" y2="1">
        <stop offset="0" stop-color="#62ad4a"/>
        <stop offset="1" stop-color="#3b7a2a"/>
      </linearGradient>
    </defs>
    <path d="M476,0 L680,0 L680,510 L0,510 L0,438 C150,436 292,420 350,330 C400,250 408,120 476,0 Z" fill="var(--arc)"/>
    <path d="M488,0 L680,0 L680,510 L0,510 L0,446 C155,444 300,428 360,334 C410,254 420,120 488,0 Z" fill="url(#frontGreen)"/>
  </svg>

  <div class="brand">
    <span class="brand-mark"></span>
    <span class="brand-name"><span class="brand-name-main">RTM</span><span class="brand-name-sub">Groundwork Services</span></span>
  </div>

  <div class="photo photo--apartments" role="img" aria-label="Photo of orange apartment buildings"></div>
  <div class="photo photo--house" role="img" aria-label="Photo of a large suburban house with a lawn"></div>

  <div class="contact-pill">
    <div class="contact-row"><svg viewBox="0 0 10 10"><circle cx="5" cy="5" r="4.2" fill="none" stroke="#fff"/><path d="M1 5h8M5 1v8" stroke="#fff" stroke-width="0.8"/></svg>www.rtmgroundwork.com</div>
    <div class="contact-row"><svg viewBox="0 0 10 10"><rect x="0.5" y="2" width="9" height="6" fill="none" stroke="#fff"/><path d="M0.5 2l4.5 3.5 4.5-3.5" fill="none" stroke="#fff"/></svg>rtmgroundwork@postmail.com</div>
    <div class="contact-row"><svg viewBox="0 0 10 10"><circle cx="5" cy="5" r="4.2" fill="none" stroke="#fff"/><path d="M3.5 3c0 2 1.5 3.5 3.2 3.6" fill="none" stroke="#fff" stroke-width="1.1"/></svg>(609) 555-0148</div>
  </div>

  <h2 class="section-title mission-title">OUR MISSION:</h2>
  <p class="body-copy mission-copy">RTM is dedicated to the personal contact and service-oriented approach to the management of residential and commercial buildings.<br>We stand by our commitment to develop a comfortable environment for our client communities, and we will make every effort to promote the long-term growth and profitability of their real estate investments.</p>

  <p class="hours">MONDAY TO SATURDAY 7AM TO 8PM</p>
</section>
<p class="side-label side-label--front">Front</p>

<section class="card card--back" aria-label="Postcard back">
  <svg class="card-shape" viewBox="0 0 680 510" aria-hidden="true">
    <defs>
      <linearGradient id="backGreen" x1="0" y1="0" x2="1" y2="1">
        <stop offset="0" stop-color="#4f9a3a"/>
        <stop offset="1" stop-color="#3b7a2a"/>
      </linearGradient>
    </defs>
    <path d="M294,0 C342,120 356,260 370,330 C392,420 520,486 680,496" fill="none" stroke="var(--arc)" stroke-width="6"/>
    <path d="M0,0 L282,0 C330,120 344,260 358,330 C380,420 500,496 660,510 L0,510 Z" fill="url(#backGreen)"/>
  </svg>

  <h2 class="section-title services-title">OUR SERVICES:</h2>
  <p class="body-copy services-copy">RTM Management will handle the day-to-day activities that are required in operating your Association. RTM Management offers building and ground maintenance as well as operations management services to meet your association's needs. We are the best at what we do and will provide your association with the support you need and require.</p>

  <h2 class="section-title why-title">WHY CHOOSE RTM:</h2>
  <p class="body-copy why-copy">RTM is a leader in managing properties in Mercer County. The diverse client portfolio of RTM.</p>
  <ul class="checklist">
    <li>Landscaping Company.</li>
    <li>Lawn Cuts.</li>
    <li>Mulch.</li>
    <li>Spring Clean Ups.</li>
    <li>Planting.</li>
  </ul>

  <div class="photo photo--garden" role="img" aria-label="Photo of a stone house with landscaped garden and flower beds"></div>

  <h2 class="section-title clients-title">OUR CLIENT LIST:</h2>
  <ul class="client-list">
    <li class="client"><div class="client-box">Brookvale Cardiology</div><p class="client-caption">Brookvale Cardiology</p></li>
    <li class="client"><div class="client-box">Brookvale Gastro</div><p class="client-caption">Brookvale Gastroenterology</p></li>
    <li class="client"><div class="client-box">Corvane</div><p class="client-caption">Corvane Medical Offices</p></li>
    <li class="client"><div class="client-box">Harbor Point</div><p class="client-caption">Harbor Point Banks</p></li>
  </ul>

  <div class="brand">
    <span class="brand-mark"></span>
    <span class="brand-name"><span class="brand-name-main">RTM</span><span class="brand-name-sub">Groundwork Services</span></span>
  </div>
  <div class="stamp-box"></div>
  <div class="address-lines"><span></span><span></span><span></span><span></span></div>
  <address class="return-address">
    <strong>RTM GROUNDWORK SERVICES</strong>
    ADDRESS - 47 Dunmore Ln.<br>
    W. Pellston, NJ 08591<br>
    Phone #- 609-555-0148
  </address>
</section>
<p class="side-label side-label--back">Back</p>

</body>
</html>
```